Etiquetas para platos preparados de la marca Tarvelia

Necesito el diseño de una belly band o etiquetas para productos cocinados. En ella debe aparecer la siguiente información: el logo de la marca,
Símbolos con la siguiente info: refrigerado entre 2º-4º, pincha el plástico que lo cubre, imagen microondas 3:00, disfruta.
Además necesito que la etiqueta tenga en la parte frontal una zona donde podamos modificar e ir añadiendo el nombre del producto en concreto y en la parte trasera una zona destinada también a los valores nutricionales personalizable.
Por último necesitamos que las etiquetas estén diseñadas en 6 colores diferentes para poder diferenciar entre diferentes categorías (ensaladas, carnes, pescados, postres, ECO...).
Los tamaños de los envases sobre los que debe ir el belly band es el siguiente:
-Formato 1: 180x180x35mm
-Formato 2: 168x128x35mm
-Formato 3: belly band de 30cm de largo

Otro

Target Market(s)

Producto expuesto es vitrinas expositoras de supermercados

Industry/Entity Type

Alimentación

Font styles to use
Sans Serif
Other font styles liked:
• Cocomat y Poppins

Requirements
Must have
• Atractivo visualmente. Fuentes empleadas Cocomat y Montserrat
Nice to have
• Los colores para diferenciar categorías y espacio para poder incluir nosotros el nombre de cada producto. Además un espacio que ponga Origen personalizable también y un logo que ponga casero 100%

```html
<!DOCTYPE html>
<html lang="es">
<head>
<meta charset="utf-8">
<title>Tarvelia · Belly bands por categoría</title>
<link href="https://fonts.googleapis.com/css2?family=Montserrat:wght@300;400;600&display=swap" rel="stylesheet">
<style>
  :root{
    --bg-center:#fdf2e4;
    --bg-edge:#f5e3cc;
    --brand:#06414a;
    --paper:#ffffff;
    --ink:#1f4a50;
    --icon:#fdba6a;

    /* six category colours */
    --cat-fish:#4f9fcf;
    --cat-meat:#a81c22;
    --cat-salad:#4cb86d;
    --cat-dessert:#fdba6a;
    --cat-eco:#8a6bb8;
    --cat-ready:#e2698f;
  }
  *{box-sizing:border-box;margin:0;padding:0}
  html,body{width:1200px;height:971px;overflow:hidden}
  body{
    position:relative;
    font-family:"Montserrat",sans-serif;
    background:radial-gradient(ellipse at 50% 48%,var(--bg-center) 0%,var(--bg-edge) 75%);
  }

  .band{position:absolute;display:flex;background:var(--paper)}
  .band__face{position:relative;flex:1}
  .band__strip{background:var(--cat)}

  .brand-tab{
    position:absolute;top:0;
    display:flex;align-items:flex-end;justify-content:center;
    background:var(--brand);
    color:#fff;font-weight:400;letter-spacing:.05em;text-transform:uppercase;white-space:nowrap;
  }
  .product-name{
    position:absolute;text-align:right;
    color:var(--cat);font-weight:400;text-transform:uppercase;line-height:1.22;
  }
  .care-icons{position:absolute;display:flex;justify-content:space-between}
  .care-icon{display:flex;flex-direction:column;align-items:center;color:var(--icon)}
  .care-icon svg{fill:none;stroke:currentColor}
  .care-icon span{text-align:center;line-height:1.15;font-weight:400;white-space:nowrap}
  .product-art{position:absolute;right:0}
  .nutrition{
    position:absolute;border:1px solid #222;background:#fff;
    display:flex;flex-direction:column;padding:3px 3px 2px;
  }
  .nutrition__bar{height:2px;background:var(--ink)}
  .nutrition__rows{flex:1;margin:3px 0;
    background:repeating-linear-gradient(to bottom,#9fb0b2 0 1px,transparent 1px 4px)}
  .nutrition__label{font-size:3px;font-weight:600;transform:rotate(180deg);text-align:center;margin-top:2px;white-space:nowrap}

  /* small bands */
  .band--small{top:202px;width:83px;height:567px}
  .band--small .band__strip{width:21px}
  .band--small .brand-tab{left:3px;width:56px;height:45px;border-radius:0 0 12px 12px;font-size:7px;padding-bottom:16px}
  .band--small .product-name{right:3px;top:58px;font-size:9.5px}
  .band--small .care-icons{left:6px;width:52px;top:116px}
  .band--small .care-icon svg{width:8px;height:8px}
  .band--small .care-icon span{font-size:1.8px;margin-top:2px}
  .band--small .product-art{top:133px;width:28px;height:100px}
  .band--small .nutrition{left:5px;top:392px;width:52px;height:71px}

  /* featured band */
  .band--large{left:729px;top:292px;width:139px;height:388px}
  .band--large .band__strip{width:36px}
  .band--large .brand-tab{left:5px;width:93px;height:76px;border-radius:0 0 20px 20px;font-size:12px;padding-bottom:28px}
  .band--large .product-name{right:5px;top:100px;font-size:17px}
  .band--large .care-icons{left:8px;width:80px;top:196px}
  .band--large .care-icon svg{width:13px;height:13px}
  .band--large .care-icon span{font-size:3px;margin-top:3px}
  .band--large .product-art{top:236px;width:73px;height:130px}

  /* category modifiers */
  .fish{--cat:var(--cat-fish)}
  .meat{--cat:var(--cat-meat)}
  .salad{--cat:var(--cat-salad)}
  .dessert{--cat:var(--cat-dessert)}
  .eco{--cat:var(--cat-eco)}
  .ready{--cat:var(--cat-ready)}
</style>
</head>
<body>

<!-- Pescados -->
<section class="band band--small fish" style="left:75px">
  <div class="band__face">
    <div class="brand-tab">Tarvelia</div>
    <h2 class="product-name">Salmón<br>al<br>horno</h2>
    <div class="care-icons">
      <div class="care-icon"><svg viewBox="0 0 10 10" stroke-width="1"><path d="M5 0v10M0.7 2.5l8.6 5M0.7 7.5l8.6-5"/></svg><span>Refrigerado 2°-4°</span></div>
      <div class="care-icon"><svg viewBox="0 0 10 10" stroke-width="1"><path d="M4 9V2.5a1 1 0 0 1 2 0V5l2 .6V9z"/></svg><span>Pincha el plástico</span></div>
      <div class="care-icon"><svg viewBox="0 0 12 10" stroke-width="1"><rect x="0.5" y="1.5" width="11" height="7"/><path d="M8 1.5v7"/></svg><span>3:00 y disfruta</span></div>
    </div>
    <div class="product-art" role="img" aria-label="Ilustración de un pescado en azul" style="background:linear-gradient(90deg,transparent,#7fb9de 40%,#4f9fcf);border-radius:60% 0 0 60%"></div>
    <div class="nutrition"><div class="nutrition__bar"></div><div class="nutrition__rows"></div><div class="nutrition__bar"></div><div class="nutrition__label">Información nutricional</div></div>
  </div>
  <div class="band__strip"></div>
</section>

<!-- Carnes -->
<section class="band band--small meat" style="left:196px">
  <div class="band__face">
    <div class="brand-tab">Tarvelia</div>
    <h2 class="product-name">Carne<br>de<br>res</h2>
    <div class="care-icons">
      <div class="care-icon"><svg viewBox="0 0 10 10" stroke-width="1"><path d="M5 0v10M0.7 2.5l8.6 5M0.7 7.5l8.6-5"/></svg><span>Refrigerado 2°-4°</span></div>
      <div class="care-icon"><svg viewBox="0 0 10 10" stroke-width="1"><path d="M4 9V2.5a1 1 0 0 1 2 0V5l2 .6V9z"/></svg><span>Pincha el plástico</span></div>
      <div class="care-icon"><svg viewBox="0 0 12 10" stroke-width="1"><rect x="0.5" y="1.5" width="11" height="7"/><path d="M8 1.5v7"/></svg><span>3:00 y disfruta</span></div>
    </div>
    <div class="product-art" role="img" aria-label="Ilustración de un corte de carne en rojo" style="top:140px;height:86px;background:linear-gradient(90deg,#c9565b,#a81c22);border-radius:50% 0 0 50%"></div>
    <div class="nutrition"><div class="nutrition__bar"></div><div class="nutrition__rows"></div><div class="nutrition__bar"></div><div class="nutrition__label">Información nutricional</div></div>
  </div>
  <div class="band__strip"></div>
</section>

<!-- Ensaladas -->
<section class="band band--small salad" style="left:315px">
  <div class="band__face">
    <div class="brand-tab">Tarvelia</div>
    <h2 class="product-name">Ensalada<br>Cesar</h2>
    <div class="care-icons">
      <div class="care-icon"><svg viewBox="0 0 10 10" stroke-width="1"><path d="M5 0v10M0.7 2.5l8.6 5M0.7 7.5l8.6-5"/></svg><span>Refrigerado 2°-4°</span></div>
      <div class="care-icon"><svg viewBox="0 0 10 10" stroke-width="1"><path d="M4 9V2.5a1 1 0 0 1 2 0V5l2 .6V9z"/></svg><span>Pincha el plástico</span></div>
      <div class="care-icon"><svg viewBox="0 0 12 10" stroke-width="1"><rect x="0.5" y="1.5" width="11" height="7"/><path d="M8 1.5v7"/></svg><span>3:00 y disfruta</span></div>
    </div>
    <div class="product-art" role="img" aria-label="Ilustración de un plato de ensalada en verde" style="top:138px;width:34px;height:84px;background:radial-gradient(circle at 100% 50%,#8fd3a4,#4cb86d 70%);border-radius:42px 0 0 42px"></div>
    <div class="nutrition"><div class="nutrition__bar"></div><div class="nutrition__rows"></div><div class="nutrition__bar"></div><div class="nutrition__label">Información nutricional</div></div>
  </div>
  <div class="band__strip"></div>
</section>

<!-- Postres -->
<section class="band band--small dessert" style="left:434px">
  <div class="band__face">
    <div class="brand-tab">Tarvelia</div>
    <h2 class="product-name">Pay<br>de<br>limón</h2>
    <div class="care-icons">
      <div class="care-icon"><svg viewBox="0 0 10 10" stroke-width="1"><path d="M5 0v10M0.7 2.5l8.6 5M0.7 7.5l8.6-5"/></svg><span>Refrigerado 2°-4°</span></div>
      <div class="care-icon"><svg viewBox="0 0 10 10" stroke-width="1"><path d="M4 9V2.5a1 1 0 0 1 2 0V5l2 .6V9z"/></svg><span>Pincha el plástico</span></div>
      <div class="care-icon"><svg viewBox="0 0 12 10" stroke-width="1"><rect x="0.5" y="1.5" width="11" height="7"/><path d="M8 1.5v7"/></svg><span>3:00 y disfruta</span></div>
    </div>
    <div class="product-art" role="img" aria-label="Ilustración de un pastel con cobertura en naranja" style="top:142px;width:44px;height:78px;background:linear-gradient(180deg,#fdba6a,#fedcb0)"></div>
    <div class="nutrition"><div class="nutrition__bar"></div><div class="nutrition__rows"></div><div class="nutrition__bar"></div><div class="nutrition__label">Información nutricional</div></div>
  </div>
  <div class="band__strip"></div>
</section>

<!-- Banda destacada -->
<section class="band band--large dessert">
  <div class="band__face">
    <div class="brand-tab">Tarvelia</div>
    <h2 class="product-name">Donas<br>de<br>azúcar</h2>
    <div class="care-icons">
      <div class="care-icon"><svg viewBox="0 0 10 10" stroke-width="1"><path d="M5 0v10M0.7 2.5l8.6 5M0.7 7.5l8.6-5"/></svg><span>Refrigerado<br>entre 2°-4°</span></div>
      <div class="care-icon"><svg viewBox="0 0 10 10" stroke-width="1"><path d="M4 9V2.5a1 1 0 0 1 2 0V5l2 .6V9z"/></svg><span>Pincha el plástico<br>que lo cubre</span></div>
      <div class="care-icon"><svg viewBox="0 0 12 10" stroke-width="1"><rect x="0.5" y="1.5" width="11" height="7"/><path d="M8 1.5v7"/></svg><span>3:00 y Disfruta</span></div>
    </div>
    <div class="product-art" role="img" aria-label="Ilustración de un pastel con cobertura en naranja" style="background:linear-gradient(180deg,#fdba6a,#fee2bf)"></div>
  </div>
  <div class="band__strip"></div>
</section>

</body>
</html>
```